Wedding Startup Full Website Design

We've just completed our online platform and need to create a website that represents our brand and vision, and clearly communicates our features and value proposition to potential users. There are a minimum of 4 pages that need to be designed. One geared toward wedding professionals (venues/vendors/coordinators), another toward engaged couples, one showcasing features, and an 'About Us' page.

The designer will creative freedom to create a unique UI/UX as long as it represents our brand and is relevant to our target audience/market. The ideal candidate will be able to assume the mindset of someone working in the wedding industry and/or an engaged couple. Ability to create illustrations is a plus.

Copy will be provided as needed. We will reimburse for stock images (pending approval before purchasing), but sourcing the stock images will be the responsibility of the designer.

Our current website: https://www.trelmora.com
Updates

Our project has now been guaranteed! We look forward to finding the perfect design for our site pages!

Still waiting for a design that stands out from the rest and aligns with the creative brief.

Target Market(s)

Wedding Professionals and Engaged Couples

Industry/Entity Type

Wedding

Number of Pages Required

4 page

Font styles to use
Sans Serif

Colors
ffffff
fbd4d5
f59195
33a6d7
cadf82
86cfc6

Requirements
Must have
• Common sense stuff like having a unified brand that accurately represents our platform, speaks to our target market, and clearly articulates our vision
Nice to have
• Illustrations
Should not have
• Overly cheesy or childish. We want to be professional but still embrace the wedding culture.

```html
<!DOCTYPE html>
<html lang="en">
<head>
<meta charset="utf-8">
<title>Trelmora — Smarter Wed Planning</title>
<link href="https://fonts.googleapis.com/css2?family=Raleway:wght@200;300;400;500;600&display=swap" rel="stylesheet">
<style>
  :root{
    --white:#ffffff;
    --blush:#fbd4d5;
    --coral:#f48789;
    --blue:#6fb1e1;
    --sky:#d6e8f6;
    --ink:#3b3b3b;
    --muted:#8a8a8a;
    --line:#e4e4e4;
  }
  *{box-sizing:border-box;margin:0;padding:0}
  html,body{width:1200px;height:1200px;overflow:hidden;background:var(--white)}
  body{font-family:'Raleway',sans-serif;color:var(--ink)}
  .page{position:absolute;left:461px;top:0;width:278px;height:1200px;overflow:hidden;background:var(--white)}
  .shapes{position:absolute;left:0;top:0;width:278px;height:1200px}
  .abs{position:absolute}

  .site-nav .brand{left:17px;top:5px;font-size:8px;font-weight:400;color:var(--blue)}
  .site-nav ul{list-style:none;left:147px;top:8px;display:flex;gap:6px;font-size:3px}
  .site-nav li.active{color:var(--coral);border-bottom:0.5px solid var(--coral)}
  .site-nav .search{left:224px;top:7px;width:4px;height:4px;border:0.5px solid var(--ink);border-radius:50%}
  .site-nav .demo-btn{left:234px;top:6px;width:30px;height:8px;background:var(--coral);color:var(--white);font-size:2.6px;display:flex;align-items:center;justify-content:center;letter-spacing:.1px}

  .hero-copy{left:17px;top:79px;color:var(--white)}
  .hero-copy .eyebrow{font-size:3.6px;font-weight:400}
  .hero-copy h1{font-size:14px;font-weight:200;margin-top:3px;line-height:1}
  .hero-copy .tagline{font-size:7.5px;font-weight:200;opacity:.85;margin-top:1px}
  .hero-copy .cta{font-size:3.4px;margin-top:5px}

  h2.section-title{font-weight:200;color:var(--ink);line-height:1.05}
  .steps-title{left:29px;top:221px;font-size:16px}
  .step{width:60px}
  .step h3{font-size:4px;font-weight:500}
  .step p{font-size:2.4px;color:var(--muted);line-height:1.35;margin-top:1.5px}
  .step .cta{font-size:3px;color:var(--blue);margin-top:3px}

  .mission-copy{left:110px;top:378px;width:128px}
  .mission-copy h2{font-size:16px}
  .mission-copy p{font-size:4.6px;line-height:1.45;margin-top:4px;color:#4a3030}
  .mission-copy .cta{font-size:3.2px;font-weight:600;margin-top:6px}

  .why-title{left:17px;top:596px;font-size:16px}
  .feature{width:66px}
  .feature .icon{width:11px;height:11px}
  .feature h3{font-size:4px;font-weight:500;margin-top:3px}
  .feature p{font-size:2.4px;color:var(--muted);line-height:1.35;margin-top:1.5px}

  .start-copy{left:149px;top:840px;width:116px}
  .start-copy h2{font-size:16px}
  .start-copy p{font-size:4.6px;line-height:1.45;margin-top:6px;color:#4a3030}
  .start-copy .cta{font-size:3.2px;font-weight:600;margin-top:5px}

  .socials{left:0;top:1044px;width:278px;display:flex;justify-content:center;gap:7px}
  .socials span{width:12px;height:12px;border-radius:50%;background:var(--white);box-shadow:0 0.5px 2px rgba(0,0,0,.18)}
  .footer-nav{left:0;top:1069px;width:278px;display:flex;justify-content:center;gap:7px;font-size:2.6px;color:var(--muted);list-style:none}
  .copyright{left:0;top:1190px;width:278px;text-align:center;font-size:2.4px;color:var(--muted)}
</style>
</head>
<body>
<div class="page">
  <svg class="shapes" viewBox="0 0 278 1200" xmlns="http://www.w3.org/2000/svg">
    <defs>
      <radialGradient id="illustration-tone" cx=".55" cy=".45" r=".65">
        <stop offset="0" stop-color="#9fd6d8"/><stop offset=".35" stop-color="#5fb9bd"/>
        <stop offset=".7" stop-color="#3d9ea5"/><stop offset="1" stop-color="#2b8089"/>
      </radialGradient>
      <linearGradient id="bride-tone" x1="0" y1="0" x2="0" y2="1">
        <stop offset="0" stop-color="#dbe5ee"/><stop offset=".25" stop-color="#e8eef4"/>
        <stop offset=".6" stop-color="#f1f5f9"/><stop offset="1" stop-color="#d6e6f3"/>
      </linearGradient>
      <linearGradient id="winter-tone" x1="0" y1="0" x2="0" y2="1">
        <stop offset="0" stop-color="#ffffff"/><stop offset=".32" stop-color="#eef2f5"/>
        <stop offset=".52" stop-color="#a9bac6"/><stop offset=".66" stop-color="#536b79"/>
        <stop offset=".76" stop-color="#6b8290"/><stop offset=".8" stop-color="#e6edf2"/>
        <stop offset="1" stop-color="#eef3f7"/>
      </linearGradient>
      <radialGradient id="portrait-tone" cx=".22" cy=".45" r=".7">
        <stop offset="0" stop-color="#9a9a9a"/><stop offset=".3" stop-color="#c4c4c4"/>
        <stop offset=".65" stop-color="#e2e2e2"/><stop offset="1" stop-color="#f7f7f7"/>
      </radialGradient>
      <linearGradient id="portrait-fade" x1="0" y1="0" x2="0" y2="1">
        <stop offset="0" stop-color="#fff" stop-opacity="1"/><stop offset=".75" stop-color="#fff" stop-opacity="1"/>
        <stop offset="1" stop-color="#fff" stop-opacity="0"/>
      </linearGradient>
      <mask id="portrait-mask"><rect x="0" y="812" width="278" height="230" fill="url(#portrait-fade)"/></mask>
      <linearGradient id="party-tone" x1="0" y1="0" x2="0" y2="1">
        <stop offset="0" stop-color="#eef1ec"/><stop offset=".3" stop-color="#7f9170"/>
        <stop offset=".55" stop-color="#a9ad94"/><stop offset=".75" stop-color="#ece7e2"/>
        <stop offset=".9" stop-color="#8c6a70"/><stop offset="1" stop-color="#6b7a55"/>
      </linearGradient>
    </defs>

    <!-- hero -->
    <path d="M0,30 C40,16 95,30 140,60 C175,90 200,150 215,180 C235,205 275,200 278,190 L278,200 C245,215 190,205 150,186 C100,170 40,180 0,190 Z" fill="var(--sky)"/>
    <g role="img" aria-label="Illustration of a wedding planner at her desk dreaming of a dress, cake and bouquet">
      <path d="M135,72 C145,40 185,18 228,22 C262,26 278,40 278,40 L278,168 C262,182 235,190 205,188 C170,186 145,165 136,135 C130,115 130,92 135,72 Z" fill="url(#illustration-tone)"/>
    </g>
    <path d="M0,50 C25,36 75,30 108,42 C138,55 142,85 130,112 C116,142 82,165 42,174 C22,178 8,176 0,172 Z" fill="var(--blue)"/>

    <!-- steps progress -->
    <line x1="30" y1="251" x2="194" y2="251" stroke="var(--line)" stroke-width="0.8"/>
    <line x1="30" y1="251" x2="86" y2="251" stroke="var(--blue)" stroke-width="1.4"/>
    <circle cx="34" cy="251" r="2.2" fill="var(--blue)"/>
    <circle cx="106" cy="251" r="1.4" fill="var(--white)" stroke="var(--line)" stroke-width="0.5"/>
    <circle cx="178" cy="251" r="1.4" fill="var(--white)" stroke="var(--line)" stroke-width="0.5"/>

    <!-- mission -->
    <path d="M0,420 C20,360 60,330 112,345 C170,370 210,440 200,480 C175,525 110,560 40,558 C20,557 8,553 0,550 Z" fill="var(--sky)"/>
    <g role="img" aria-label="Soft faded photo of a bride in a flowing gown">
      <path d="M0,430 C10,380 40,345 70,345 C95,350 105,400 100,460 C96,510 80,545 50,556 C25,556 8,552 0,550 Z" fill="url(#bride-tone)"/>
    </g>
    <path d="M278,325 C240,305 160,312 110,345 C75,370 68,420 80,460 C95,510 140,535 180,528 C220,520 255,490 278,465 Z" fill="var(--coral)"/>

    <!-- why -->
    <g role="img" aria-label="Photo of a wedding couple embracing in a snowy pine forest">
      <rect x="0" y="636" width="278" height="176" fill="url(#winter-tone)"/>
    </g>

    <!-- get started -->
    <g role="img" aria-label="Black and white photo of a smiling bride with a veil" mask="url(#portrait-mask)">
      <rect x="0" y="812" width="278" height="230" fill="url(#portrait-tone)"/>
    </g>
    <path d="M278,802 C245,795 175,800 140,826 C110,850 105,905 115,945 C128,985 170,990 210,972 C245,955 265,935 278,918 Z" fill="var(--sky)"/>
    <path d="M278,815 C240,800 170,805 130,830 C100,850 92,900 100,940 C110,975 150,990 190,975 C230,960 262,930 278,910 Z" fill="var(--coral)"/>

    <!-- footer -->
    <g role="img" aria-label="Photo of a bride with her bridesmaids holding bouquets in a garden">
      <rect x="0" y="1076" width="278" height="110" fill="url(#party-tone)"/>
    </g>
  </svg>

  <header class="site-nav">
    <div class="abs brand">Trelmora</div>
    <ul class="abs">
      <li class="active">Home</li><li>About us</li><li>Features</li><li>For couples</li>
    </ul>
    <div class="abs search"></div>
    <div class="abs demo-btn">ACCESS DEMO</div>
  </header>

  <section class="abs hero-copy">
    <div class="eyebrow">Welcome to</div>
    <h1>Trelmora</h1>
    <div class="tagline">Smarter Wed Planning™</div>
    <div class="cta">Get Started →</div>
  </section>

  <h2 class="abs section-title steps-title">How To Get Started</h2>
  <div class="abs step" style="left:31px;top:256px">
    <h3>Sign Up</h3>
    <p>Create a free account on Trelmora to access popular collaboration tools.</p>
    <div class="cta">Get Started →</div>
  </div>
  <div class="abs step" style="left:103px;top:256px">
    <h3>Collaborate</h3>
    <p>Add clients within the application to better organize and manage event details.</p>
  </div>
  <div class="abs step" style="left:174px;top:256px">
    <h3>Connect</h3>
    <p>Linking your bank account within Trelmora to allow for seamless payments and tendering.</p>
  </div>

  <section class="abs mission-copy">
    <h2 class="section-title">Mission<br>Statement</h2>
    <p>Weddings are one the most memorable events in people's life. Unfortunately planning a wedding is filled with stress, often leaving wedding professionals and their clients with soured memories.</p>
    <div class="cta">Learn More About Us →</div>
  </section>

  <h2 class="abs section-title why-title">Why Trelmora</h2>
  <div class="abs feature" style="left:17px;top:626px">
    <svg class="icon" viewBox="0 0 12 12"><circle cx="6" cy="6" r="4.5" fill="none" stroke="#333" stroke-width=".7"/><path d="M6,3.5 V6 L4.5,7.5" fill="none" stroke="#333" stroke-width=".7"/></svg>
    <h3>Saves Everyone Time</h3>
    <p>Trelmora streamlines certain processes allowing you to spend more time on the things your event is all about.</p>
  </div>
  <div class="abs feature" style="left:102px;top:626px">
    <svg class="icon" viewBox="0 0 12 12"><g fill="none" stroke="#333" stroke-width=".6"><rect x="4.5" y="1.5" width="3" height="2.5"/><rect x="1" y="8" width="2.5" height="2.5"/><rect x="4.75" y="8" width="2.5" height="2.5"/><rect x="8.5" y="8" width="2.5" height="2.5"/><path d="M6,4 V8 M2.25,8 V6 H9.75 V8"/></g></svg>
    <h3>Simplified Organization</h3>
    <p>Trelmora was built with organization in mind. All event details are in one place making executing an event easier.</p>
  </div>
  <div class="abs feature" style="left:187px;top:626px">
    <svg class="icon" viewBox="0 0 12 12"><path d="M3,10 V5.5 H4.5 L6.5,2 C7.5,2 7.6,3 7.3,4.5 H9.8 C10.4,4.5 10.6,5.2 10.3,6 L9.2,9.4 C9,9.8 8.7,10 8.3,10 Z" fill="none" stroke="#333" stroke-width=".6"/></svg>
    <h3>Better Client Reviews</h3>
    <p>With Trelmora you can offer your clients an experience they will rave about, leading to better reviews and more clients.</p>
  </div>
  <div class="abs feature" style="left:17px;top:674px">
    <svg class="icon" viewBox="0 0 12 12"><g fill="none" stroke="#333" stroke-width=".7"><rect x="1.5" y="1.5" width="6" height="8.5"/><rect x="6.5" y="5" width="4" height="6"/></g></svg>
    <h3>Accessible on Any Device</h3>
    <p>Flexibility is key, which is why Trelmora's platform was built to be accessed on your phone, tablet or desktop.</p>
  </div>
  <div class="abs feature" style="left:102px;top:674px">
    <svg class="icon" viewBox="0 0 12 12"><g fill="none" stroke="#333" stroke-width=".6"><rect x="1.5" y="3" width="9" height="6.5"/><circle cx="6" cy="6.25" r="1.6"/><path d="M3,2 H9"/></g></svg>
    <h3>Lower Transaction Fees</h3>
    <p>We offer the lowest transaction fees in the wedding industry, meaning you keep more of your money.</p>
  </div>

  <section class="abs start-copy">
    <h2 class="section-title">Get Started<br>Today</h2>
    <p>We recently launched a demo version of Trelmora to allow users to see and interact with our platform. Create a free account and see how Trelmora is changing the wedding planning process!</p>
    <div class="cta">Get Started →</div>
  </section>

  <div class="abs socials"><span></span><span></span><span></span><span></span></div>
  <ul class="abs footer-nav">
    <li>HOME</li><li>ABOUT US</li><li>FEATURES</li><li>FOR COUPLES</li><li>CAREER</li><li>CONTACT US</li>
  </ul>
  <div class="abs copyright">© trelmora 2017-2018. All rights reserved.</div>
</div>
</body>
</html>
```